Business Card cabinets and cabinets components making company.

the card should be formal and interesting at the same time. The main colors will be black and white.

Font styles to use
Sans Serif

Colors

Designer to choose only greyscale colors for use in the design.

Requirements
Must have
• At least must have the followings:
office phone
cell phone
address
position
name
email
web

```html
<!DOCTYPE html>
<html lang="en">
<head>
<meta charset="UTF-8">
<title>Joinwell Business Card</title>
<link href="https://fonts.googleapis.com/css2?family=Poppins:wght@400;500;600;700&display=swap" rel="stylesheet">
<style>
  :root {
    --canvas: #ececec;
    --card-white: #ffffff;
    --card-black: #1c1c1c;
    --ink: #1a1a1a;
    --accent: #f26a21;
    --muted-on-black: #3a3a3a;
  }
  * { box-sizing: border-box; margin: 0; padding: 0; }
  html, body {
    width: 1200px; height: 1050px; overflow: hidden;
    background: var(--canvas);
    font-family: "Poppins", sans-serif;
  }
  .sheet {
    width: 1200px; height: 1050px;
    display: flex; flex-direction: column; align-items: center; justify-content: center;
    gap: 60px;
  }
  .card {
    width: 700px; height: 400px; border-radius: 22px;
    position: relative; overflow: hidden;
    box-shadow: 0 10px 30px rgba(0,0,0,0.12);
  }
  .card--front {
    background: var(--card-white);
    display: flex; align-items: center;
    padding: 0 50px;
  }
  .brand {
    width: 300px;
    display: flex; align-items: center; gap: 14px;
  }
  .brand__square {
    width: 26px; height: 26px; background: var(--accent);
  }
  .brand__name {
    font-weight: 700; font-size: 52px; color: var(--ink);
    letter-spacing: -1px; line-height: 1;
  }
  .divider {
    width: 2px; height: 200px; background: var(--accent);
    margin: 0 28px 0 20px;
  }
  .contact { color: var(--ink); }
  .contact__name {
    font-weight: 700; font-size: 24px; letter-spacing: 0.5px; text-transform: uppercase;
  }
  .contact__role {
    color: var(--accent); font-size: 15px; margin-bottom: 6px;
  }
  .contact__address { font-size: 15px; line-height: 1.4; margin-bottom: 4px; }
  .contact__list { list-style: none; font-size: 15px; line-height: 1.55; }
  .contact__list li { display: flex; align-items: center; gap: 10px; }
  .contact__list svg { width: 14px; height: 14px; flex: none; }
  .web-accent { color: var(--accent); }
  .card--back {
    background: var(--card-black);
    display: flex; align-items: center; justify-content: center; gap: 18px;
  }
  .card--back .brand__name { color: var(--muted-on-black); font-size: 72px; }
  .card--back .brand__square { width: 36px; height: 36px; }
</style>
</head>
<body>
<main class="sheet">
  <section class="card card--front">
    <div class="brand">
      <span class="brand__square"></span>
      <span class="brand__name">Joinwell</span>
    </div>
    <div class="divider"></div>
    <div class="contact">
      <h1 class="contact__name">Mara Elden</h1>
      <p class="contact__role">President</p>
      <p class="contact__address">4410 Birchwood Lane #118<br>Lakeview, FL 33710</p>
      <ul class="contact__list">
        <li>
          <svg viewBox="0 0 24 24" fill="none" stroke="#f26a21" stroke-width="2.2"><path d="M5 3h4l2 5-2.5 1.5a11 11 0 0 0 6 6L16 13l5 2v4a2 2 0 0 1-2 2A16 16 0 0 1 3 5a2 2 0 0 1 2-2z"/></svg>
          +1 (555) 014 2270
        </li>
        <li>
          <svg viewBox="0 0 24 24" fill="none" stroke="#f26a21" stroke-width="2.2"><rect x="6" y="2" width="12" height="20" rx="2"/><line x1="11" y1="18" x2="13" y2="18"/></svg>
          +1 (555) 014 2271
        </li>
        <li>
          <svg viewBox="0 0 24 24" fill="none" stroke="#f26a21" stroke-width="2.2"><rect x="2" y="5" width="20" height="14" rx="1"/><path d="M2 6l10 7 10-7"/></svg>
          hello@joinwellcab.com
        </li>
        <li>
          <svg viewBox="0 0 24 24" fill="none" stroke="#f26a21" stroke-width="2.2"><circle cx="12" cy="12" r="10"/><path d="M2 12h20M12 2a15 15 0 0 1 0 20M12 2a15 15 0 0 0 0 20"/></svg>
          www.<span class="web-accent">joinwellcab</span>.com
        </li>
      </ul>
    </div>
  </section>

  <section class="card card--back">
    <span class="brand__square"></span>
    <span class="brand__name">Joinwell</span>
  </section>
</main>
</body>
</html>
```